Business Card Design

We need a business card design for an existing business. Our main trading brand is www.brightmeadowsaver.co.uk

We attach various logo files - please use the version that will produce the sharpest image on the business card.

We are flexible about shape of card etc. Please think outside the box as to what goes on front and what goes on back of the card

We want to be able to amend the card (once the design has been agreed ) to add additional staff details, but the text to go on it will be generic

Details to go on card ( for the first generic one) are fairly minimal as we don't like cluttered business cards:-

Tom Harker
Managing Director

Mobile: 07812 548 207
Email: t.harker@brightmeadowsaver.co.uk

```html
<!DOCTYPE html>
<html lang="en">
<head>
<meta charset="utf-8">
<title>Bright Meadow Saver – Business Card</title>
<link href="https://fonts.googleapis.com/css2?family=Lato:wght@300;400;700;900&display=swap" rel="stylesheet">
<style>
  :root {
    --bg: #e9e9ea;
    --card-green: #a9d86e;
    --card-green-deep: #9acb5f;
    --brand-blue: #1f86d1;
    --ink: #2f3a2a;
    --ink-soft: #4a5640;
    --icon: #24507a;
  }
  * { box-sizing: border-box; margin: 0; padding: 0; }
  html, body {
    width: 1200px; height: 750px; overflow: hidden;
    background: var(--bg);
    font-family: "Lato", Arial, sans-serif;
  }
  .canvas {
    position: relative; width: 1200px; height: 750px;
    background: radial-gradient(ellipse at 50% 40%, #f3f3f4 0%, var(--bg) 70%);
  }
  .card {
    position: absolute; left: 120px; top: 225px;
    width: 960px; height: 300px;
  }
  .card-shape { position: absolute; inset: 0; }
  .brand {
    position: absolute; left: 150px; top: 168px;
    display: flex; align-items: center; gap: 12px;
  }
  .brand-dot {
    width: 22px; height: 22px; border-radius: 50%;
    background: var(--brand-blue);
  }
  .brand-name {
    font-weight: 700; font-size: 34px; color: var(--brand-blue);
    letter-spacing: 0.2px;
  }
  .contact {
    position: absolute; left: 610px; top: 72px;
    color: var(--ink);
  }
  .contact-name {
    font-size: 30px; text-transform: uppercase; letter-spacing: 0.5px;
  }
  .contact-name .first { font-weight: 900; }
  .contact-name .last { font-weight: 300; }
  .contact-role {
    font-size: 13px; color: var(--ink-soft); margin-top: 2px; margin-bottom: 18px;
  }
  .contact-line {
    display: flex; align-items: center; gap: 10px;
    font-size: 15px; margin-bottom: 10px;
  }
  .contact-line svg { flex: none; }
</style>
</head>
<body>
<main class="canvas">
  <section class="card" aria-label="Business card">
    <svg class="card-shape" viewBox="0 0 960 300" width="960" height="300" aria-hidden="true">
      <polygon points="0,0 880,0 960,150 880,300 0,300 80,150" fill="var(--card-green)"/>
      <circle cx="190" cy="215" r="85" fill="var(--card-green-deep)" opacity="0.6"/>
    </svg>

    <div class="brand">
      <span class="brand-dot"></span>
      <span class="brand-name">brightmeadowsaver.co.uk</span>
    </div>

    <div class="contact">
      <h1 class="contact-name"><span class="first">Tom</span> <span class="last">Harker</span></h1>
      <p class="contact-role">Managing Director</p>
      <p class="contact-line">
        <svg width="14" height="18" viewBox="0 0 14 18" aria-label="Mobile">
          <rect x="1" y="1" width="12" height="16" rx="2" fill="none" stroke="var(--icon)" stroke-width="1.6"/>
          <circle cx="7" cy="14" r="1" fill="var(--icon)"/>
        </svg>
        <span>07812 548 207</span>
      </p>
      <p class="contact-line">
        <svg width="16" height="12" viewBox="0 0 16 12" aria-label="Email">
          <rect x="0" y="0" width="16" height="12" rx="1" fill="var(--icon)"/>
          <polyline points="1,1 8,7 15,1" fill="none" stroke="var(--card-green)" stroke-width="1.2"/>
        </svg>
        <span>t.harker@brightmeadowsaver.co.uk</span>
      </p>
    </div>
  </section>
</main>
</body>
</html>
```